fast and fun ive already created the site, i need someone to clean it up and make it professional

I have a plexo website that looks and feels a lot like what I would like, I think I just need someone to expand on what is already there.

Please re-make the logo (this is especially important) , the fonts, the background, and the pictures on all of the site, so the site is better and more cohesive

To take a look at it please go to plexo.net
log in: itsdanielhoward@mailvero.net
password = 749213Kq
website = "paw-field-classic"

(please don't erase anything and do not use this plexo account for creating your submission)

You can create your own PLEXO account and send pdfs or links to me as your submission.

I want you to make a "PLEXO Website" = very important

target market: women,
feelings required: love, sports, dogs, happiness

thank you!

dan

Reason: I'm extending the deadline to allow more time for everyone.

Industry/Entity Type

It Professional

Font styles to use
Sans Serif

Requirements
Must have
• change the logo

```html
<!DOCTYPE html>
<html lang="en">
<head>
<meta charset="utf-8">
<title>Paw Sprinters</title>
<link href="https://fonts.googleapis.com/css2?family=Anton&family=Arimo:wght@400;700&display=swap" rel="stylesheet">
<style>
  :root {
    --sand: #e9e4da;
    --white: #ffffff;
    --green: #84c41f;
    --blue: #2a98cf;
    --blue-deep: #1f7fb3;
    --teal: #1a9fcf;
    --ink: #1e1e1e;
    --text: #3a3a3a;
    --dots: #6d6d6d;
  }
  * { margin: 0; padding: 0; box-sizing: border-box; }
  html, body { width: 1200px; height: 1030px; overflow: hidden; }
  body {
    position: relative;
    background: var(--sand);
    font-family: "Arimo", Arial, sans-serif;
    color: var(--text);
  }
  .header { position: absolute; left: 0; top: 0; width: 1200px; height: 121px; background: var(--sand); border-top: 2px solid #cfcac0; z-index: 2; }
  .brand { position: absolute; left: 214px; top: 58px; display: flex; align-items: center; gap: 8px; }
  .brand-dot { width: 18px; height: 18px; border-radius: 50%; background: var(--teal); }
  .brand-name { font-weight: 700; font-size: 18px; color: var(--green); }
  .nav { position: absolute; left: 445px; top: 48px; width: 567px; height: 25px; }
  .nav text { font-family: "Arimo", Arial, sans-serif; font-size: 12.5px; fill: var(--white); }
  .dropdown {
    position: absolute; left: 873px; top: 76px; width: 139px; height: 52px;
    background: var(--blue-deep); border-radius: 0 0 6px 6px;
    list-style: none; text-align: center; padding-top: 5px;
  }
  .dropdown li { font-size: 12.5px; color: var(--white); line-height: 20px; }

  .hero { position: absolute; left: 0; top: 121px; width: 1200px; height: 416px; background: var(--white); border-bottom: 1px solid #d8d3c9; z-index: 1; }
  .hero-photo { position: absolute; left: 203px; top: 19px; width: 515px; height: 379px; background: linear-gradient(180deg, #5f7a4a 0%, #6f9a4a 30%, #5b8a38 70%, #4f7c30 100%); }
  .dotted { position: absolute; border-top: 2px dotted var(--dots); }
  .hero-title { position: absolute; left: 745px; top: 42px; font-family: "Anton", Impact, sans-serif; font-size: 50px; line-height: 52px; color: var(--ink); letter-spacing: -0.5px; }
  .hero-sub { position: absolute; left: 747px; top: 217px; width: 280px; font-size: 29px; line-height: 37px; color: var(--ink); }
  .hero-next { position: absolute; left: 848px; top: 334px; width: 70px; height: 70px; border-radius: 50%; background: var(--green); }

  .principles { position: absolute; left: 204px; top: 560px; width: 400px; }
  .section-title { font-size: 26px; font-weight: 700; color: var(--teal); display: flex; align-items: center; gap: 6px; }
  .spark { color: var(--white); font-size: 16px; }
  .principles ul { margin: 14px 0 0 38px; list-style: disc; font-size: 12.2px; line-height: 15px; color: var(--text); }
  .principles li { margin-bottom: 15px; padding-left: 4px; }
  .divider-v { position: absolute; left: 622px; top: 568px; height: 263px; border-left: 2px dotted var(--teal); }

  .runner { position: absolute; left: 657px; width: 360px; }
  .runner-photo { position: absolute; left: 0; top: 0; width: 94px; height: 94px; border-radius: 50%; border: 2px solid #cfc8bb; }
  .runner-title { position: absolute; left: 106px; font-size: 16px; font-weight: 700; color: var(--teal); display: flex; gap: 6px; align-items: center; white-space: nowrap; }
  .runner-text { position: absolute; left: 130px; width: 228px; font-size: 11px; line-height: 12.5px; color: var(--ink); }

  .divider-h { position: absolute; left: 206px; top: 866px; width: 814px; border-top: 2px dotted var(--dots); }

  .footer { position: absolute; left: 0; top: 898px; width: 1200px; height: 132px; background: var(--green); }
  .footer-links { position: absolute; left: 202px; top: 52px; display: flex; align-items: center; gap: 30px; list-style: none; }
  .footer-item { display: flex; align-items: center; gap: 6px; font-size: 11px; font-weight: 700; color: var(--white); white-space: nowrap; }
  .footer-item.copyright { margin-right: 20px; }
  .social-dot { flex: 0 0 12px; width: 12px; height: 12px; border-radius: 50%; background: var(--white); }
</style>
</head>
<body>
  <header class="header">
    <div class="brand">
      <span class="brand-dot"></span>
      <span class="brand-name">Paw Sprinters</span>
    </div>
    <svg class="nav" viewBox="0 0 567 25" aria-label="Main navigation">
      <polygon points="0,0 140,0 148,12.5 140,25 0,25 5,12.5" fill="#84c41f"/>
      <polygon points="140,0 281,0 289,12.5 281,25 140,25 148,12.5" fill="#2a98cf"/>
      <polygon points="281,0 421,0 429,12.5 421,25 281,25 289,12.5" fill="#2a98cf"/>
      <path d="M421,0 H561 A6,6 0 0 1 567,6 V19 A6,6 0 0 1 561,25 H421 L429,12.5 Z" fill="#2a98cf"/>
      <polyline points="140,0 148,12.5 140,25" fill="none" stroke="#fff" stroke-width="1.2"/>
      <polyline points="281,0 289,12.5 281,25" fill="none" stroke="#fff" stroke-width="1.2"/>
      <polyline points="421,0 429,12.5 421,25" fill="none" stroke="#fff" stroke-width="1.2"/>
      <text x="74" y="17" text-anchor="middle">Home</text>
      <text x="213" y="17" text-anchor="middle">Services &amp; Rates</text>
      <text x="354" y="17" text-anchor="middle">Our Runners</text>
      <text x="495" y="17" text-anchor="middle">More</text>
    </svg>
    <ul class="dropdown">
      <li>FAQ</li>
      <li>Contact Us</li>
    </ul>
  </header>

  <section class="hero">
    <div class="hero-photo" role="img" aria-label="Photo of a dog running across a grassy field"></div>
    <div class="dotted" style="left:751px; top:32px; width:263px;"></div>
    <h1 class="hero-title">When you<br>feel dog<br>tired,</h1>
    <p class="hero-sub">it's because you ran with The Paw Sprinters</p>
    <div class="dotted" style="left:752px; top:366px; width:80px;"></div>
    <div class="dotted" style="left:934px; top:366px; width:80px;"></div>
    <div class="hero-next">
      <svg width="70" height="70" viewBox="0 0 70 70" aria-hidden="true">
        <polyline points="30,22 43,35 30,48" fill="none" stroke="#fff" stroke-width="3"/>
      </svg>
    </div>
  </section>

  <section class="principles">
    <h2 class="section-title"><span class="spark">✦</span>Our Principles</h2>
    <ul>
      <li>We are passionate about what we do.</li>
      <li>Your dog's needs, health and safety come before anything else.</li>
      <li>We will perform our services with honesty, integrity and respect.</li>
      <li>We aim for your complete and total satisfaction, if there is ever any way that we can serve you better we will do our best to find a way to do it.</li>
      <li>We are grateful for being a part our community and grateful for you our customers.</li>
      <li>We take pride in being able to offer you high quality services.</li>
    </ul>
  </section>
  <div class="divider-v"></div>

  <article class="runner" style="top:568px;">
    <div class="runner-photo" role="img" aria-label="Round photo of the runner of the week" style="background: radial-gradient(circle, #d9a36a 0%, #b77d4a 55%, #8fa0c9 100%);"></div>
    <h3 class="runner-title" style="top:3px;"><span class="spark">✦</span>Runner of the week</h3>
    <p class="runner-text" style="top:27px;">Lorem ipsum dolor sit amet, consectetur adipisicing elit, sed do eiusmod tempor incididunt ut labore et dolore magna aliqua. Ut enim ad minim veniam, quis nostrude Lorem ipsum.</p>
  </article>

  <article class="runner" style="top:715px;">
    <div class="runner-photo" role="img" aria-label="Round photo of the runner of the month" style="background: radial-gradient(circle, #d9b48a 0%, #7d9a4e 60%, #4f7a2e 100%);"></div>
    <h3 class="runner-title" style="top:-10px;"><span class="spark">✦</span>Runner of the month</h3>
    <p class="runner-text" style="top:30px;">Lorem ipsum dolor sit amet, consectetur adipisicing elit, sed do eiusmod tempor incididunt ut labore et dolore magna aliqua. Ut enim ad minim veniam, quis nostrude Lorem ipsum.</p>
  </article>

  <div class="divider-h"></div>

  <footer class="footer">
    <ul class="footer-links">
      <li class="footer-item copyright"><span>✦</span>© 2013 Paw Sprinters, All Rights Reserved</li>
      <li class="footer-item"><span class="social-dot"></span>Follow Us on Chirpline</li>
      <li class="footer-item"><span class="social-dot"></span>Follow us on Friendbook</li>
      <li class="footer-item"><span class="social-dot"></span>Paw Sprinters on ViewTube</li>
    </ul>
  </footer>
</body>
</html>
```